New label for vitamin and supplement products

We are a a Vitamin and Supplement company called Bright Harbor. We have been in business for 30 years and the branding needs a significant refresh.

We need all new packaging, including logo, colors, etc.

We want to have a fresh, clean, brand that inspires confidence and quality.

The website is Brightharbor.com and will also be updated.

Please ask any questions. Every idea is a good one.

```html
<!DOCTYPE html>
<html lang="en">
<head>
<meta charset="utf-8">
<title>Bright Harbor — Beta Carotene Labels</title>
<link rel="stylesheet" href="https://fonts.googleapis.com/css2?family=Questrial&family=Fira+Sans+Condensed:wght@400;500&display=swap">
<style>
  :root {
    --navy: #22487a;
    --navy-light: #35639c;
    --sky: #a9cdee;
    --label-blue: #7eaedb;
    --label-blue-deep: #5f8fbf;
    --purple: #7667a8;
    --purple-deep: #655593;
    --purple-text: #6a58a8;
    --white: #ffffff;
    --paper: #f1f2f4;
    --ink: #1e1e22;
    --charcoal: #4a4a4c;
  }
  * { margin: 0; padding: 0; box-sizing: border-box; }
  html, body { width: 1200px; height: 879px; overflow: hidden; }
  body {
    position: relative;
    background: var(--navy);
    font-family: "Questrial", sans-serif;
  }
  .backdrop { position: absolute; inset: 0; }

  .brand-tab {
    position: absolute; left: 817px; top: 0; width: 200px; height: 140px;
    display: flex; align-items: center; justify-content: center; gap: 8px;
  }
  .brand-tab .mark { width: 12px; height: 12px; background: var(--sky); }
  .brand-tab .name {
    font-family: "Questrial", sans-serif; font-size: 26px; color: var(--sky);
    letter-spacing: 1px;
  }

  .label {
    position: absolute; top: 372px; width: 288px; height: 346px;
    overflow: hidden; border-radius: 4px; background: var(--paper);
  }
  .label-white { left: 152px; }
  .label-purple { left: 476px; }

  .label > div, .label .tab > div { position: absolute; line-height: 1; white-space: nowrap; }

  .brand-name { font-family: "Questrial", sans-serif; letter-spacing: .5px; }
  .natural { right: 36px; font-family: "Fira Sans Condensed", sans-serif; font-size: 20px; }
  .product {
    left: 0; right: 0; text-align: center;
    font-family: "Questrial", sans-serif; font-size: 27px; letter-spacing: .3px;
  }
  .subtitle {
    left: 0; right: 0; text-align: center;
    font-family: "Fira Sans Condensed", sans-serif; font-weight: 500; font-size: 18px;
  }
  .dose { font-family: "Fira Sans Condensed", sans-serif; font-size: 19px; text-align: center; }
  .dose small { display: block; font-size: 11px; margin-top: 3px; }
  .supplement { font-family: "Fira Sans Condensed", sans-serif; font-size: 12px; }
  .label .count {
    color: var(--white); text-align: center;
    display: flex; flex-direction: column; justify-content: center; align-items: center;
  }
  .count b { font-weight: 400; font-size: 22px; }
  .count span { font-size: 11px; margin-top: 3px; }

  .label-white .brand-name { left: 38px; top: 40px; font-size: 15px; color: var(--label-blue-deep); }
  .label-white .natural { top: 92px; color: var(--label-blue-deep); }
  .label-white .product { top: 116px; color: var(--ink); }
  .label-white .subtitle { top: 160px; color: var(--ink); }
  .label-white .dose { left: 40px; top: 222px; color: var(--label-blue-deep); }
  .label-white .band {
    left: 0; right: 0; top: 258px; height: 72px;
    background: linear-gradient(90deg, var(--label-blue), var(--label-blue-deep));
  }
  .label-white .supplement { left: 34px; top: 278px; color: var(--white); }
  .label-white .count {
    left: 178px; top: 236px; width: 66px; height: 66px; border-radius: 50%;
    background: var(--charcoal);
  }

  .label-purple .top {
    left: 0; right: 0; top: 0; height: 256px;
    background: linear-gradient(90deg, var(--purple), var(--purple-deep));
  }
  .label-purple .tab {
    position: absolute; left: 62px; top: 0; width: 164px; height: 28px;
    background: var(--paper); border-radius: 0 0 12px 12px;
  }
  .label-purple .brand-name {
    left: 0; right: 0; top: 8px; text-align: center; font-size: 14px; color: var(--purple-text);
  }
  .label-purple .natural { top: 98px; color: var(--ink); }
  .label-purple .product { top: 122px; color: var(--white); }
  .label-purple .subtitle { top: 164px; color: var(--white); }
  .label-purple .dose { left: 0; right: 0; top: 198px; color: var(--ink); }
  .label-purple .count {
    left: 97px; top: 240px; width: 78px; height: 58px; border-radius: 8px;
    background: var(--charcoal);
  }
  .label-purple .supplement {
    left: 0; right: 0; top: 310px; text-align: center; color: var(--purple-text);
  }

  .headline { position: absolute; left: 816px; top: 424px; color: var(--white); }
  .headline h1 {
    font-family: "Questrial", sans-serif; font-weight: 400; font-size: 38px;
    letter-spacing: 1px; line-height: 1;
  }
  .headline p {
    font-family: "Fira Sans Condensed", sans-serif; font-weight: 500;
    font-size: 27px; margin-top: 14px;
  }
</style>
</head>
<body>
  <svg class="backdrop" width="1200" height="879" viewBox="0 0 1200 879" aria-hidden="true">
    <path d="M1085 0 L1200 0 L1200 879 L580 879 C480 840 360 790 300 752 L300 520 C520 470 760 400 880 330 C1040 240 1130 130 1085 0 Z" fill="var(--navy-light)"/>
  </svg>

  <div class="brand-tab">
    <span class="mark"></span>
    <span class="name">Bright Harbor</span>
  </div>

  <section class="label label-white">
    <div class="brand-name">BRIGHT HARBOR</div>
    <div class="natural">NATURAL</div>
    <div class="product">BETA CAROTENE</div>
    <div class="subtitle">PROVITAMIN A</div>
    <div class="dose">3,000 mcg<small>(10,000 IU)</small></div>
    <div class="band"></div>
    <div class="supplement">DIETARY SUPPLEMENT</div>
    <div class="count"><b>60</b><span>Capsules</span></div>
  </section>

  <section class="label label-purple">
    <div class="top"></div>
    <div class="tab"><div class="brand-name">BRIGHT HARBOR</div></div>
    <div class="natural">NATURAL</div>
    <div class="product">BETA CAROTENE</div>
    <div class="subtitle">PROVITAMIN A</div>
    <div class="dose">3,000 mcg<small>(10,000 IU)</small></div>
    <div class="count"><b>60</b><span>Capsules</span></div>
    <div class="supplement">DIETARY SUPPLEMENT</div>
  </section>

  <div class="headline">
    <h1>BETA CAROTENE</h1>
    <p>PROVITAMIN A</p>
  </div>
</body>
</html>
```